Criação de Folder para Viagens & Lazer
" Realizo trabalhos voltado para definiçoes de processo, implantação e melhoria da qualidade e eficiencia operacional. realizo projetos de implantação de usinas de beneficiamento de algodão além de treinamentos e palestras no seguimento de beneficiamento e qualidade do algodão. o Nome VI-NORBA NÃO É REGISTRADO E PODE SE TORNAR UM NOME DE RAZAÇÃO SOCIAL E CRIARMOS UM NOVO NOME FANTASIA "

```html
<!DOCTYPE html>
<html lang="pt-BR">
<head>
<meta charset="utf-8">
<title>Folder Vi-Norba</title>
<link href="https://fonts.googleapis.com/css2?family=Pinyon+Script&family=Montserrat:wght@400;500;600;700;800&display=swap" rel="stylesheet">
<style>
:root{
  --navy:#1b2b57;
  --blue:#3f7fc1;
  --sky:#a8c6e6;
  --mist:#e8eef6;
  --paper:#ffffff;
  --ink:#2b3346;
  --muted:#5d667a;
  --backdrop:#eceff3;
}
*{margin:0;padding:0;box-sizing:border-box}
html,body{width:1200px;height:1200px;overflow:hidden;background:var(--backdrop);font-family:"Montserrat",sans-serif;color:var(--ink)}
.spread{position:absolute;left:30px;top:197px;width:1140px;height:806px;display:flex;box-shadow:0 10px 30px rgba(20,30,60,.18)}
.panel{position:relative;width:570px;height:806px;overflow:hidden;background:var(--paper)}
.panel--about{border-right:1px solid #dde3ec}
.ornaments{position:absolute;left:60px;top:40px;width:150px;height:210px;border-radius:10px;background:linear-gradient(160deg,var(--navy),var(--blue) 60%,var(--sky))}
.about-photo{position:absolute;left:0;bottom:0;width:570px;height:430px;background:linear-gradient(180deg,rgba(255,255,255,0),#c9d2de 55%,#aeb9c8)}
.script-title{font-family:"Pinyon Script",cursive;color:var(--navy);font-weight:400}
.about-title{position:absolute;left:250px;top:44px;font-size:54px}
.about-text{position:absolute;left:250px;top:128px;width:280px;font-size:12.5px;line-height:1.6;color:var(--ink)}
.about-text strong{color:var(--navy);font-weight:800}
.brand-tab{position:absolute;left:0;top:430px;width:170px;height:120px;background:var(--navy);border-radius:0 60px 60px 0;display:flex;align-items:center;gap:10px;padding-left:22px}
.brand-dot{width:22px;height:22px;border-radius:50%;background:var(--paper)}
.brand-name{color:var(--paper);font-weight:800;font-size:17px;letter-spacing:.5px}
.highlights{position:absolute;left:215px;top:440px;width:320px;list-style:none}
.highlights li{display:flex;gap:14px;align-items:flex-start;margin-bottom:22px;font-size:12.5px;line-height:1.5;color:var(--ink);font-weight:500}
.hl-icon{flex:0 0 34px;height:34px;border-radius:8px;background:var(--navy);display:flex;align-items:center;justify-content:center}
.panel--services{display:flex}
.services{position:relative;flex:1;padding:44px 0 0 38px}
.services-title{font-size:52px;margin-bottom:24px}
.service{display:flex;gap:18px;margin-bottom:22px}
.service-photo{flex:0 0 118px;height:94px;border-radius:10px}
.service h3{font-size:14px;font-weight:800;color:var(--navy);margin:6px 0 6px}
.service p{font-size:12px;line-height:1.5;color:var(--muted)}
.pattern-strip{flex:0 0 118px;height:100%;background:linear-gradient(180deg,var(--navy),var(--blue) 35%,var(--sky) 55%,var(--navy) 80%,var(--blue))}
</style>
</head>
<body>
<main class="spread">
  <section class="panel panel--about">
    <div class="about-photo" role="img" aria-label="Foto esmaecida de plantação de algodão ao fundo"></div>
    <div class="ornaments" role="img" aria-label="Ornamentos geométricos em tons de azul"></div>
    <h1 class="script-title about-title">A Vi-Norba</h1>
    <p class="about-text"><strong>A VI-NORBA</strong> é uma empresa especializada em consultoria para usinas de beneficiamento de algodão. Com anos de experiência no setor, oferece soluções completas em processos, qualidade e eficiência operacional, unindo conhecimento técnico, treinamento de equipes e acompanhamento próximo para garantir o melhor custo-benefício para nossos clientes.</p>
    <div class="brand-tab"><span class="brand-dot"></span><span class="brand-name">VI-NORBA</span></div>
    <ul class="highlights">
      <li><span class="hl-icon"><svg width="18" height="18" viewBox="0 0 18 18"><circle cx="9" cy="9" r="7" fill="none" stroke="#fff" stroke-width="2"/><path d="M9 5v4l3 2" stroke="#fff" stroke-width="2" fill="none"/></svg></span>Mais de 25 anos de atuação no segmento do algodão.</li>
      <li><span class="hl-icon"><svg width="18" height="18" viewBox="0 0 18 18"><path d="M3 9l4 4 8-8" stroke="#fff" stroke-width="2.2" fill="none"/></svg></span>Soluções personalizadas para maximizar a eficiência, produtividade e qualidade.</li>
      <li><span class="hl-icon"><svg width="18" height="18" viewBox="0 0 18 18"><rect x="3" y="3" width="5" height="5" fill="#fff"/><rect x="10" y="3" width="5" height="5" fill="#fff"/><rect x="3" y="10" width="5" height="5" fill="#fff"/><rect x="10" y="10" width="5" height="5" fill="#fff"/></svg></span>Propostas moduladas para que o cliente escolha as etapas que deseja contratar.</li>
      <li><span class="hl-icon"><svg width="18" height="18" viewBox="0 0 18 18"><path d="M9 2l6 3v4c0 4-3 6-6 7-3-1-6-3-6-7V5z" fill="none" stroke="#fff" stroke-width="2"/></svg></span>Práticas que aliam segurança, qualidade e compromisso com o meio ambiente.</li>
    </ul>
  </section>
  <section class="panel panel--services">
    <div class="services">
      <h2 class="script-title services-title">O que fazemos ?</h2>
      <article class="service">
        <div class="service-photo" role="img" aria-label="Foto de linha de máquinas em usina de algodão" style="background:linear-gradient(135deg,#c9a24a,#6f7f93)"></div>
        <div><h3>Assessoria Especializada</h3><p>Avaliação completa das operações<br>Identificação dos pontos de melhoria<br>Planos com etapas de execução</p></div>
      </article>
      <article class="service">
        <div class="service-photo" role="img" aria-label="Foto de equipamentos instalados em usina" style="background:linear-gradient(135deg,#d8c070,#7c8a9a)"></div>
        <div><h3>Instalação e Partida de Usinas</h3><p>Dicas para aquisição de equipamentos<br>Definição dos parâmetros de segurança<br>DataVista personalizado para gestão</p></div>
      </article>
      <article class="service">
        <div class="service-photo" role="img" aria-label="Foto de equipe em treinamento de processos" style="background:linear-gradient(135deg,#9fb3c8,#4b5e78)"></div>
        <div><h3>Padronização de Processos</h3><p>Implementação de procedimentos<br>Definição de parâmetros de qualidade<br>Treinamentos operacionais</p></div>
      </article>
      <article class="service">
        <div class="service-photo" role="img" aria-label="Foto de técnico calibrando equipamento" style="background:linear-gradient(135deg,#b7a27a,#5b6472)"></div>
        <div><h3>Calibração dos Equipamentos</h3><p>Criar planejamento de manutenções<br>Ajustes para produção de sementes<br>Programa de manutenção preventiva</p></div>
      </article>
      <article class="service">
        <div class="service-photo" role="img" aria-label="Foto de análise de amostras de algodão em laboratório" style="background:linear-gradient(135deg,#a8b8cc,#56657d)"></div>
        <div><h3>Análise de Dados</h3><p>Coleta e análise de dados<br>Análise de umidade e temperatura<br>Melhorias no rendimento de pluma</p></div>
      </article>
    </div>
    <div class="pattern-strip" role="img" aria-label="Faixa de padrão geométrico em azul-marinho, azul e azul-claro"></div>
  </section>
</main>
</body>
</html>
```